Stationery Design needed for logo design project

This company needs a letterhead and envelope for their new practice. We did not want to release this contact until the business card design was finalized so the stationary can be created to coordinate with it.

For those of you that will be submitting designs for this content, think "linear". Designs with curves or "swooshes" are not appropriate for this design.

NOTE: As part of the source files; I will require FULLY LAYERED PHOTOSHOP FILES of all elements, including design elements, text and fonts. If you cannot provide a fully layered PSD file, please do not submit.
Updates

The project details have been updated. We have added a new description along with logo files and business card design. Please review the style of the logo and business card before submitting designs. Thanks

Target Market(s)

Medical

Industry/Entity Type

Business

Requirements
Must have
• NOTE: As part of the source files; I will require FULLY LAYERED PHOTOSHOP FILES of all elements, including design elements, text and fonts. If you cannot provide a fully layered PSD file, please do not submit.

Logo
2 office address locations
phone
fax
email
website URL

```html
<!DOCTYPE html>
<html lang="en">
<head>
<meta charset="utf-8">
<title>Linden &amp; Partners Letterhead</title>
<link href="https://fonts.googleapis.com/css2?family=Tinos:ital,wght@0,400;0,700;1,400&family=Open+Sans:wght@400;600&display=swap" rel="stylesheet">
<style>
  :root {
    --backdrop: #dcdcdc;
    --paper: #ffffff;
    --ink: #1c1c1c;
    --ink-soft: #555555;
    --brand-red: #b3141c;
    --signature-tone: #c9c9c9;
  }
  * { box-sizing: border-box; margin: 0; padding: 0; }
  html, body {
    width: 1200px; height: 909px; overflow: hidden;
    background: var(--backdrop);
  }
  .letterhead {
    position: absolute; left: 280px; top: 38px;
    width: 640px; height: 832px;
    background: var(--paper);
    box-shadow: 0 6px 24px rgba(0,0,0,.18);
    font-family: "Tinos", "Times New Roman", serif;
    color: var(--ink);
  }
  .brand {
    position: absolute; top: 52px; left: 0; right: 0;
    display: flex; justify-content: center; align-items: center; gap: 10px;
  }
  .brand-mark { width: 14px; height: 14px; background: var(--brand-red); }
  .brand-text { display: flex; flex-direction: column; }
  .brand-name {
    font-family: "Tinos", serif; font-size: 22px; letter-spacing: 1px;
    color: var(--ink); line-height: 1;
  }
  .brand-tagline {
    font-family: "Open Sans", sans-serif; font-size: 7px; letter-spacing: 1.5px;
    text-transform: uppercase; color: var(--brand-red); margin-top: 3px;
  }
  .letter-body {
    position: absolute; top: 150px; left: 72px; width: 496px;
    font-size: 12.5px; line-height: 1.42; text-align: justify;
  }
  .letter-body p { margin-bottom: 13px; }
  .salutation { margin-bottom: 14px !important; }
  .closing { margin-top: 28px; line-height: 1.35; }
  .signature {
    display: block; width: 120px; height: 34px; margin: 8px 0 4px;
    background: linear-gradient(90deg, var(--signature-tone), #e6e6e6);
    border-radius: 3px;
  }
  .contact {
    position: absolute; left: 72px; bottom: 60px;
    font-family: "Open Sans", sans-serif; font-size: 9px; line-height: 1.55;
    color: var(--ink-soft);
  }
  .contact-address { margin-bottom: 6px; }
  .contact-line { display: flex; align-items: center; gap: 6px; }
  .contact-line svg { width: 9px; height: 9px; fill: var(--brand-red); }
  .web-tab {
    position: absolute; right: 0; bottom: 96px;
    width: 150px; height: 24px; background: var(--brand-red);
    border-radius: 6px 0 0 0;
    display: flex; align-items: center; justify-content: center;
    font-family: "Open Sans", sans-serif; font-size: 9px; color: #fff; letter-spacing: .5px;
  }
</style>
</head>
<body>
<main class="letterhead">
  <header class="brand">
    <span class="brand-mark"></span>
    <div class="brand-text">
      <span class="brand-name">LINDEN &amp; PARTNERS</span>
      <span class="brand-tagline">Cardiology and Wellness</span>
    </div>
  </header>

  <section class="letter-body">
    <p class="salutation">Gentlemen,</p>
    <p>Enclosed I have the honor to send you an article which I should be pleased if you would accept for the &ldquo;Harbor Review&rdquo;. I am <em>desperately</em> pushed for money; and in the event of Mr. Hartley&rsquo;s liking the &ldquo;Landscape-Garden&rdquo; I would take it as an especial favor if you would mail me the amount due for it, so as to reach me here by the 21st, on which day I shall need it. Can you possibly oblige me in this? If you accept the paper I presume you will allow me your usual sum, whatever that is for similar contributions&mdash;but I set no price&mdash;leaving all to your own liberality. The piece will make 8 of your pages and rather more.</p>
    <p>Will you be kind enough to put the best possible interpretation upon my behavior while in N-York? You must have conceived a <em>queer</em> idea of me&mdash;but the simple truth is that Mr. Brandt would insist upon <em>the juleps</em>, and I knew not what I was either doing or saying. The Review of Pell which I offered you was deficient in a &frac12; page of commencement, which I had written to supersede the old beginning, and which gave the article the character of a general and retrospective review. No wonder you did not take it&mdash;I would have been very much mortified if you had. I hope to see you at some future time, under better auspices.</p>
    <p class="closing">In the meantime I remain<br>Yours very truly,</p>
    <span class="signature" role="img" aria-label="Handwritten signature"></span>
    <p>Edwin A. Marsh</p>
  </section>

  <footer class="contact">
    <div class="contact-address">PO Box 218<br>Fairhaven, VT 05743</div>
    <div class="contact-address">PO Box 218<br>Fairhaven, VT 05743</div>
    <div class="contact-line">
      <svg viewBox="0 0 10 10"><path d="M2 1h2l1 2.5-1.2.8a5 5 0 0 0 1.9 1.9l.8-1.2L9 6v2a1 1 0 0 1-1 1A7 7 0 0 1 1 2a1 1 0 0 1 1-1z"/></svg>
      <span>(555) 014-2230</span>
    </div>
    <div class="contact-line">
      <svg viewBox="0 0 10 10"><path d="M2 1h2l1 2.5-1.2.8a5 5 0 0 0 1.9 1.9l.8-1.2L9 6v2a1 1 0 0 1-1 1A7 7 0 0 1 1 2a1 1 0 0 1 1-1z"/></svg>
      <span>(555) 014-2231</span>
    </div>
    <div class="contact-line">
      <svg viewBox="0 0 10 10"><path d="M1 2h8v6H1z M1 2l4 3 4-3" fill="none" stroke="#b3141c" stroke-width="1"/></svg>
      <span>clara@lindenpartners.com</span>
    </div>
  </footer>

  <div class="web-tab">www.lindenpartners.com</div>
</main>
</body>
</html>
```